Medical business needs responsive Bootstrap theme design

We need a responsive Twitter Bootstrap theme for a hair transplant business in South Korea which looks good from full size desktop screens down to smartphone displays. We would like the site to match in style with our brochure design (see the PDF and Adobe Illustrator files), although it does not need to match exactly. Please feel free to use the design elements and images in the brochure. The general flow of the theme is shown in the wireframe image.
We expect graphic design, images, CSS, and HTML. No PHP/backend/ecommerce integration is expected.
Here are the links to the 3 stock images in the brochure:
http://www.pixelvantry.com/pic.mhtml?id=918270563
http://www.lumoframes.com/photo/hair-transplant-gm730418256-61920475
http://www.lumoframes.com/photo/doctor-inspecting-skin-of-head-gm842067319-57301846
You can use the Bootstrap template here as a starting point: http://kelvarnlayouts.com/template-overviews/agency/
Target Market(s)
Our primary customers will be Westerners aged 28-45
Industry/Entity Type
Plastic Surgery
Coding
Coded - Design and coding required
Number of Pages Required
1 page

```html
<!DOCTYPE html>
<html lang="en">
<head>
<meta charset="utf-8">
<title>Hanbit Follicle Clinic</title>
<link rel="stylesheet" href="https://fonts.googleapis.com/css2?family=Open+Sans:wght@400;600;700&family=Roboto+Condensed:wght@400;700&family=Lora:ital,wght@1,400;1,700&display=swap">
<style>
:root{
  --blue:#2f8fd8;
  --blue-dark:#1f6fb2;
  --ink:#333;
  --muted:#666;
  --dark:#2f2f2f;
  --darker:#262626;
  --black:#151515;
  --light:#f2f2f2;
  --white:#fff;
}
*{box-sizing:border-box;margin:0;padding:0}
html,body{width:1200px;height:5217px;overflow:hidden}
body{font-family:"Open Sans",Arial,sans-serif;color:var(--ink);font-size:14px;background:var(--white)}
section,header,footer{position:relative;width:1200px;overflow:hidden}
.abs{position:absolute}
.title{font-family:"Roboto Condensed",Arial,sans-serif;font-size:40px;font-weight:400;color:var(--blue);text-transform:uppercase;text-align:center;width:100%;letter-spacing:1px}
.title.light{color:var(--white)}
.btn{display:inline-block;background:var(--blue);color:var(--white);font-size:13px;font-weight:600;text-transform:uppercase;border-radius:3px;text-align:center;line-height:34px;height:34px}
.btn-center{left:555px;width:90px}
.para{font-size:14px;line-height:24px;color:var(--muted)}
.photo{border-radius:2px}

/* hero */
.hero{height:574px;background:linear-gradient(90deg,#c9c9c9 0%,#8c8c8c 40%,#5a5a5a 62%,#b8b0a8 100%)}
.hero-photo{left:0;top:0;width:1200px;height:574px;background:radial-gradient(ellipse at 85% 45%,#d6c3b0 0%,rgba(120,110,100,.4) 35%,transparent 60%),linear-gradient(180deg,rgba(255,255,255,.25),rgba(0,0,0,.35))}
.topbar{left:0;top:0;width:1200px;height:120px;background:linear-gradient(180deg,rgba(255,255,255,.92),rgba(255,255,255,.55))}
.brand{left:92px;top:40px;display:flex;align-items:center;gap:12px;font-size:19px;color:var(--blue-dark);font-weight:600}
.brand-mark{width:54px;height:54px;border-radius:50%;border:4px solid var(--blue)}
.nav{right:90px;top:56px;display:flex;gap:34px;font-size:13px;font-weight:600;text-transform:uppercase;color:#444}
.nav .active{color:var(--blue);border-bottom:2px solid var(--blue);padding-bottom:8px}
.hero-title{left:375px;top:258px;font-family:"Lora",Georgia,serif;font-style:italic;font-size:42px;color:var(--white);letter-spacing:1px;text-shadow:0 2px 4px rgba(0,0,0,.5)}
.hero-text{left:385px;top:318px;width:420px;color:var(--white);font-size:15px;line-height:23px}

/* newsletter */
.newsletter{height:156px;background:var(--dark)}
.nl-label{left:105px;top:52px;font-family:"Roboto Condensed",Arial,sans-serif;font-size:40px;color:var(--blue)}
.field{background:var(--white);border-radius:2px;color:#999;font-size:13px;padding-left:12px;line-height:42px;height:42px}
.nl-name{left:340px;top:57px;width:310px}
.nl-email{left:664px;top:57px;width:313px}
.nl-btn{left:990px;top:61px;width:116px}

/* about */
.about{height:390px;background:var(--white)}
.about-deco{left:300px;top:40px;width:300px;height:300px;border-radius:50%;border:30px solid rgba(47,143,216,.06)}
.about .title{text-align:left;left:80px;top:64px;width:auto}
.about-text{left:80px;top:140px;width:720px}
.about-btn{left:80px;top:274px;width:110px}
.about-photo{left:800px;top:70px;width:400px;height:320px;background:radial-gradient(ellipse at 55% 30%,#d9b89c 0%,#9a8a80 35%,#3c4a5e 70%,#e9e9e9 100%)}

/* why */
.why{height:438px;background:linear-gradient(180deg,#3a3a3a,#2a2a2a)}
.why .title{top:70px}
.why-col{top:165px;width:330px;color:var(--white)}
.why-head{display:flex;align-items:center;gap:16px;font-family:"Roboto Condensed",Arial,sans-serif;font-size:21px;text-transform:uppercase}
.icon-circle{width:76px;height:76px;border-radius:50%;border:4px solid var(--white);display:flex;align-items:center;justify-content:center}
.why-text{margin-top:22px;font-size:13px;line-height:22px;color:#ddd}

/* method */
.method{height:946px;background:linear-gradient(180deg,#f7f7f7,#ececec)}
.method .title{top:52px}
.method-sub{left:400px;top:112px;width:400px;text-align:center;color:var(--blue);font-size:14px;line-height:22px}
.subhead{width:100%;text-align:center;font-size:19px;font-weight:700;color:var(--blue-dark);text-decoration:underline}
.step{font-size:13px;line-height:22px;color:var(--muted)}
.ph-strip{background:linear-gradient(180deg,#e9c9ad,#b87d58);border:1px solid #ddd}
.ph-tool{background:linear-gradient(135deg,#7a7a7a,#d3d3d3);border:1px solid #ccc}
.ph-skin{background:radial-gradient(circle,#e5b99a,#c98a65);border:1px solid #ccc}
.arrow{width:20px;height:44px}

/* blog */
.blog{height:678px;background:linear-gradient(180deg,#3b3b3b,#2b2b2b)}
.blog .title{top:48px}
.card{top:226px;width:330px;height:330px;background:var(--white);border:4px solid #ddd}
.card-photo{height:168px}
.card-bar{background:var(--black);color:var(--white);height:46px;display:flex;justify-content:space-between;align-items:center;padding:0 14px;font-family:"Lora",Georgia,serif;font-style:italic}
.card-bar b{font-size:20px}
.card-bar span{font-size:13px}
.card-text{padding:14px;font-size:14px;line-height:22px;color:#555}
.blog-btn{top:606px}

/* comparison */
.compare{height:477px;background:var(--light)}
.compare .title{top:62px}
.cmp{top:129px;width:315px}
.cmp-photo{height:160px;background:linear-gradient(90deg,#b28f78 0%,#8b6c5b 49%,#c9a891 51%,#9c7b66 100%)}
.cmp-bar{background:#2d2d2d;color:var(--white);font-size:13px;text-align:center}
.cmp-bar .row{display:flex;justify-content:space-around;padding:10px 20px 6px;text-transform:uppercase}
.cmp-bar .note{padding-bottom:10px}
.compare-btn{top:404px}

/* testimonials */
.testimonials{height:723px;background:var(--white)}
.testimonials .title{top:75px}
.t-sub{width:100%;text-align:center;top:133px;font-size:12px;font-weight:700;text-transform:uppercase}
.quote{top:184px;width:470px;height:393px;color:var(--white);text-align:center;padding:150px 50px 0}
.quote-mark{position:absolute;left:215px;width:40px;color:var(--blue);font-family:"Lora",Georgia,serif;font-size:56px;line-height:40px}
.quote p{font-size:14px;line-height:24px}
.quote .who{margin-top:18px;font-family:"Lora",Georgia,serif;font-style:italic;font-size:15px}
.testi-btn{top:622px}

/* contact */
.contact{height:445px;background:linear-gradient(180deg,#555,#444)}
.contact .title{top:70px}
.c-field{background:var(--white);color:var(--blue);font-size:13px;padding-left:10px;height:38px;line-height:38px;border-radius:2px}
.c-msg{left:609px;top:143px;width:410px;height:170px;line-height:24px;padding-top:4px}
.contact-btn{top:366px}

/* footer */
.footer{height:328px;background:var(--darker);color:#ccc}
.f-col{top:64px}
.f-head{font-size:14px;font-weight:700;color:var(--white);padding-bottom:10px;border-bottom:1px solid #555;width:200px}
.f-list{list-style:none;font-size:13px;line-height:30px;margin-top:20px}
.f-list li::before{content:"›";margin-right:8px}
.f-item{display:flex;gap:14px;font-size:13px;line-height:20px;margin-top:20px;align-items:flex-start}
.social{display:flex;gap:14px;margin-top:20px}
.social span{width:38px;height:38px;border:2px solid #ccc;border-radius:50%}
.bottom{height:62px;background:var(--black);color:#bbb;font-size:13px;text-align:center;line-height:62px}
.bottom em{font-style:normal;color:var(--blue)}
</style>
</head>
<body>

<header class="hero">
  <div class="abs hero-photo" role="img" aria-label="Salon interior with a smiling man touching his styled hair"></div>
  <div class="abs topbar"></div>
  <div class="abs brand"><span class="brand-mark"></span>Hanbit Follicle Clinic</div>
  <nav class="abs nav"><span class="active">Home</span><span>About</span><span>Method</span><span>Blog</span><span>Contact Us</span></nav>
  <h1 class="abs hero-title">Effective Hair Restoration</h1>
  <p class="abs hero-text">Lorem ipsum dolor sit amet, consectetur adipiscing elit. Aenean feugiat dictum lacus. Lorem ipsum dolor si...</p>
</header>

<section class="newsletter">
  <div class="abs nl-label">News Letter</div>
  <div class="abs field nl-name">User Name*</div>
  <div class="abs field nl-email">Email*</div>
  <div class="abs btn nl-btn">Subscribe</div>
</section>

<section class="about">
  <div class="abs about-deco"></div>
  <h2 class="abs title">About Hanbit Follicle Clinic</h2>
  <p class="abs para about-text">Lorem ipsum dolor sit amet, consectetur adipiscing elit. Aenean feugiat dictum lacus. Lorem ipsum dolor sit amet, consectetur adipiscing elit. Aenean feugiat dictum lacus. Lorem ipsum dolor sit amet, consectetur adipiscing elit. Aenean feugiat dictum lacus. Lorem ipsum dolor sit amet, consectetur adipiscing elit.</p>
  <div class="abs btn about-btn">Read More</div>
  <div class="abs about-photo" role="img" aria-label="Smiling doctor in a suit gesturing with an open hand"></div>
</section>

<section class="why">
  <h2 class="abs title light">Why Shouth Korea?</h2>
  <div class="abs why-col" style="left:87px">
    <div class="why-head"><span class="icon-circle" style="background:#6cb33f"><svg width="36" height="36" viewBox="0 0 36 36"><path d="M18 32V16M18 18c0-8 6-12 14-12-1 8-6 12-14 12zM18 22C18 15 13 11 5 11c1 7 5 11 13 11z" fill="#fff" stroke="#fff" stroke-width="2"/></svg></span>Quality of Care</div>
    <p class="why-text">Hair transplantation surgery has improved significantly over the last decade. State of the art technology ensures transplanted ...</p>
  </div>
  <div class="abs why-col" style="left:445px">
    <div class="why-head"><span class="icon-circle" style="background:#2db3a6"><svg width="36" height="36" viewBox="0 0 36 36"><circle cx="26" cy="8" r="5" fill="#fff"/><circle cx="9" cy="18" r="5" fill="#fff"/><circle cx="26" cy="28" r="5" fill="#fff"/><path d="M26 8L9 18l17 10" stroke="#fff" stroke-width="3" fill="none"/></svg></span>Convenience</div>
    <p class="why-text">You are already in South Korea or Japan; the procedure can be done in one day with follow up appointments available on request ...</p>
  </div>
  <div class="abs why-col" style="left:800px">
    <div class="why-head"><span class="icon-circle" style="background:#1f6fb2"><svg width="36" height="36" viewBox="0 0 36 36"><rect x="8" y="10" width="20" height="22" rx="6" fill="#fff"/><rect x="13" y="4" width="10" height="6" fill="#fff"/><text x="18" y="28" font-size="16" font-weight="700" text-anchor="middle" fill="#1f6fb2" font-family="Open Sans,sans-serif">$</text></svg></span>Cost Savings</div>
    <p class="why-text">The average hair transplant surgery in South Korea costs about $5,000 to $6,000 (30-40% less than if done in ...</p>
  </div>
</section>

<section class="method">
  <h2 class="abs title">Method</h2>
  <p class="abs method-sub">Lorem ipsum dolor sit amet, consectetur adipiscing elit. Aenean feugiat dictum lacus. Lorem ipsum dolor si...</p>

  <div class="abs subhead" style="top:222px">Traditional follicular unit transplant</div>
  <p class="abs step" style="left:87px;top:290px;width:270px">1. Hair on back of head is trimmed and a narrow strip is surgically removed so that hair can grow throught and camouflag the scar.</p>
  <svg class="abs arrow" style="left:190px;top:370px" viewBox="0 0 20 44"><path d="M10 0v34M2 28l8 14 8-14" stroke="#2f8fd8" stroke-width="4" fill="none"/></svg>
  <div class="abs ph-strip" style="left:87px;top:432px;width:233px;height:130px" role="img" aria-label="Scalp strip with hair follicles"></div>
  <div class="abs ph-tool" style="left:487px;top:285px;width:110px;height:122px" role="img" aria-label="Harvested scalp strip in a dish"></div>
  <div class="abs ph-skin" style="left:607px;top:285px;width:210px;height:122px" role="img" aria-label="Magnified follicular units"></div>
  <svg class="abs arrow" style="left:590px;top:420px" viewBox="0 0 20 44"><path d="M10 0v34M2 28l8 14 8-14" stroke="#2f8fd8" stroke-width="4" fill="none"/></svg>
  <p class="abs step" style="left:440px;top:480px;width:380px">2. The hair from above and below the excision is gently brought together and sutured using advanced surgical closure techniques...</p>
  <p class="abs step" style="left:765px;top:290px;width:345px">3. When the wound is healed, a fine scar line is almost completely concealed by the surrounding hair...</p>
  <svg class="abs arrow" style="left:980px;top:370px" viewBox="0 0 20 44"><path d="M10 0v34M2 28l8 14 8-14" stroke="#2f8fd8" stroke-width="4" fill="none"/></svg>
  <div class="abs ph-strip" style="left:877px;top:432px;width:229px;height:130px" role="img" aria-label="Healed scalp with hair covering the scar"></div>

  <div class="abs subhead" style="top:622px">Follicular Unit Extraction</div>
  <p class="abs step" style="left:87px;top:690px;width:270px">1. Hair on back of head is trimmed and a narrow strip is surgically removed so that hair can grow throught and camouflag the scar.</p>
  <svg class="abs arrow" style="left:190px;top:770px" viewBox="0 0 20 44"><path d="M10 0v34M2 28l8 14 8-14" stroke="#2f8fd8" stroke-width="4" fill="none"/></svg>
  <div class="abs ph-skin" style="left:87px;top:832px;width:233px;height:130px;background:linear-gradient(180deg,#fff,#e8d6c8)" role="img" aria-label="Single follicle extraction diagram"></div>
  <div class="abs ph-tool" style="left:487px;top:685px;width:110px;height:122px" role="img" aria-label="Head with small extraction sites"></div>
  <div class="abs ph-skin" style="left:607px;top:685px;width:210px;height:122px" role="img" aria-label="Magnified extracted follicles"></div>
  <svg class="abs arrow" style="left:590px;top:820px" viewBox="0 0 20 44"><path d="M10 0v34M2 28l8 14 8-14" stroke="#2f8fd8" stroke-width="4" fill="none"/></svg>
  <p class="abs step" style="left:440px;top:880px;width:380px">2. The hair from above and below the excision is gently brought together and sutured using advanced surgical closure techniques...</p>
  <p class="abs step" style="left:765px;top:690px;width:345px">3. When the wound is healed, a fine scar line is almost completely concealed by the surrounding hair...</p>
  <svg class="abs arrow" style="left:980px;top:770px" viewBox="0 0 20 44"><path d="M10 0v34M2 28l8 14 8-14" stroke="#2f8fd8" stroke-width="4" fill="none"/></svg>
  <div class="abs ph-strip" style="left:877px;top:832px;width:229px;height:130px;background:linear-gradient(180deg,#f3e3d6,#d5a98a)" role="img" aria-label="Cross section of skin layers with follicles"></div>
</section>

<section class="blog">
  <h2 class="abs title light">Blog</h2>
  <article class="abs card" style="left:80px;top:226px">
    <div class="card-photo" role="img" aria-label="Smiling blonde woman" style="background:linear-gradient(135deg,#e9dcc9,#a89b8a)"></div>
    <div class="card-bar"><b>Lorem ipsum</b><span>29 january 2016</span></div>
    <p class="card-text">Lorem ipsum dolor sit amet, consectetur adipiscing elit. Aenean feugiat dictum lacus...</p>
  </article>
  <article class="abs card" style="left:435px;top:226px">
    <div class="card-photo" role="img" aria-label="Doctor examining a patient's scalp" style="background:linear-gradient(135deg,#cfd8e0,#8a949c)"></div>
    <div class="card-bar"><b>Lorem ipsum</b><span>30 january 2016</span></div>
    <p class="card-text">Lorem ipsum dolor sit amet, consectetur adipiscing elit. Aenean feugiat dictum lacus...</p>
  </article>
  <article class="abs card" style="left:790px;top:226px">
    <div class="card-photo" role="img" aria-label="Surgeon working in a clinic" style="background:linear-gradient(135deg,#d8dde2,#7c8790)"></div>
    <div class="card-bar"><b>Lorem ipsum</b><span>29 january 2016</span></div>
    <p class="card-text">Lorem ipsum dolor sit amet, consectetur adipiscing elit. Aenean feugiat dictum lacus...</p>
  </article>
  <div class="abs btn btn-center blog-btn">Show All</div>
</section>

<section class="compare">
  <h2 class="abs title">Comparision</h2>
  <div class="abs cmp" style="left:87px">
    <div class="cmp-photo" role="img" aria-label="Balding man before and after hair restoration"></div>
    <div class="cmp-bar"><div class="row"><span>Before</span><span>/</span><span>After</span></div><div class="note">After 8 Month Treatment</div></div>
  </div>
  <div class="abs cmp" style="left:443px">
    <div class="cmp-photo" role="img" aria-label="Man with receding hairline before and after treatment"></div>
    <div class="cmp-bar"><div class="row"><span>Before</span><span>/</span><span>After</span></div><div class="note">After 6 Month Treatment</div></div>
  </div>
  <div class="abs cmp" style="left:798px">
    <div class="cmp-photo" role="img" aria-label="Top of head before and after treatment"></div>
    <div class="cmp-bar"><div class="row"><span>Before</span><span>/</span><span>After</span></div><div class="note">After 8 Month Treatment</div></div>
  </div>
  <div class="abs btn btn-center compare-btn">Show All</div>
</section>

<section class="testimonials">
  <h2 class="abs title">Testimonials</h2>
  <div class="abs t-sub">What our client say</div>
  <blockquote class="abs quote" style="left:87px;background:linear-gradient(135deg,#4a4a4a,#1e1e1e)" role="img" aria-label="Client portrait behind quote">
    <span class="quote-mark" style="top:70px">“</span>
    <p>Lorem ipsum dolor sit amet, consectetur adipiscing elit. Aenean feugiat dictum lacus.Lorem ipsum dolor sit amet, consectetur adipiscing elit. Aenean feugiat dictum lacus.</p>
    <div class="who">Lorem ipsum</div>
  </blockquote>
  <blockquote class="abs quote" style="left:643px;background:linear-gradient(135deg,#6a6a6a,#2e2e2e)" role="img" aria-label="Client portrait behind quote">
    <span class="quote-mark" style="top:70px">“</span>
    <p>Lorem ipsum dolor sit amet, consectetur adipiscing elit. Aenean feugiat dictum lacus.Lorem ipsum dolor sit amet, consectetur adipiscing elit. Aenean feugiat dictum lacus.</p>
    <div class="who">Lorem ipsum</div>
  </blockquote>
  <div class="abs btn btn-center testi-btn">Show All</div>
</section>

<section class="contact" role="img" aria-label="Faint world map behind contact form">
  <h2 class="abs title light">Contact</h2>
  <div class="abs c-field" style="left:181px;top:143px;width:414px">Name*</div>
  <div class="abs c-field" style="left:181px;top:209px;width:414px">Email*</div>
  <div class="abs c-field" style="left:181px;top:275px;width:414px">Subject*</div>
  <div class="abs c-field c-msg">Message*</div>
  <div class="abs btn btn-center contact-btn">Submit</div>
</section>

<footer class="footer">
  <div class="abs f-col" style="left:87px">
    <div class="f-head">About</div>
    <div style="width:80px;height:80px;border-radius:50%;border:5px solid #ddd;margin-top:24px"></div>
    <p style="font-size:13px;line-height:20px;margin-top:14px;width:200px">Lorem ipsum dolor sit amet, consectetur adipiscing elit....</p>
  </div>
  <div class="abs f-col" style="left:348px">
    <div class="f-head">Navigation</div>
    <div style="display:flex;gap:40px">
      <ul class="f-list"><li>HOME</li><li>ABOUT</li><li>METHOD</li></ul>
      <ul class="f-list"><li>BLOG</li><li>CONTACT US</li></ul>
    </div>
  </div>
  <div class="abs f-col" style="left:619px">
    <div class="f-head">Address</div>
    <div class="f-item"><svg width="16" height="22" viewBox="0 0 16 22"><path d="M8 21C3 14 1 11 1 8a7 7 0 0 1 14 0c0 3-2 6-7 13z" fill="#ccc"/><circle cx="8" cy="8" r="3" fill="#262626"/></svg><span>4120 Namsan Way,<br>Jung-gu, 04631, Korea</span></div>
    <div class="f-item"><svg width="18" height="14" viewBox="0 0 18 14"><rect width="18" height="14" rx="2" fill="#ccc"/><path d="M1 1l8 7 8-7" stroke="#262626" stroke-width="2" fill="none"/></svg><span>hello@hanbitfollicle<br>.example</span></div>
    <div class="f-item"><svg width="16" height="16" viewBox="0 0 16 16"><path d="M3 1l3 3-2 2c1 2 3 4 6 6l2-2 3 3-2 2C7 15 1 9 1 3z" fill="#ccc"/></svg><span>02 5550 1834</span></div>
  </div>
  <div class="abs f-col" style="left:887px">
    <div class="f-head">Follow Us</div>
    <div class="social"><span></span><span></span></div>
  </div>
</footer>
<div class="bottom">© 2015 <em>HANBIT FOLLICLE CLINIC</em> | Incorporated</div>

</body>
</html>
```